Banner Design for Holistic Clinic

We need a banner to be designed for a Holistic Clinic which treats patient using IV Nutrition therapy, IV Vitamin C therapy, Chelation therapy, Homoepathy , Accupuncture, Ayurveda. Our website is www.verdantcarehouse.in

We need the banner to show case all our services. IV Nutrition therapy, IV Vitamin C therapy, Chelation therapy, Homoepathy , Accupuncture, Ayurveda with special emphasis on IV Therapies. This will be in the front of the web page and will be used for leaflets and flex material.Ideally

I like the concept of IV infsuion bags, fruits etc. I have attached some of the pic which i liked. Please see the attachment "banner clinic july 13" But feel free to change it and bring in something better that will showcase all our services together

Target Market(s)

30 plus Adults

Industry/Entity Type

Health And Wellness

Font styles to use
Serif

Colors
acd036
f37122
33a6d7

Requirements
Must have
• Some samples are given below. It got to be colourful, yet pleasing.

```html
<!DOCTYPE html>
<html lang="en">
<head>
<meta charset="utf-8">
<title>Verdant Care House – Banner</title>
<link href="https://fonts.googleapis.com/css2?family=Barlow+Condensed:wght@500;700&family=Montserrat:ital,wght@0,400;1,400&display=swap" rel="stylesheet">
<style>
  :root {
    --page-bg: #f2f2f2;
    --banner-bg: #ffffff;
    --brand-green: #1f9a3c;
    --leaf-green: #8cc63f;
    --tagline-green: #7cbf2a;
    --pulse-red: #e3262b;
    --ink: #222222;
    --ink-soft: #444444;
  }
  * { margin: 0; padding: 0; box-sizing: border-box; }
  html, body { width: 1134px; height: 1200px; overflow: hidden; background: var(--page-bg); }
  .stage { position: relative; width: 1134px; height: 1200px; }
  .banner {
    position: absolute; left: 0; top: 348px;
    width: 1263px; height: 560px;
    transform: scale(0.8979); transform-origin: 0 0;
    background: radial-gradient(ellipse at 30% 60%, #ffffff 0%, #f6f6f6 60%, #eeeeee 100%);
    overflow: hidden;
  }
  .photo { position: absolute; }
  .photo--citrus {
    left: 0; top: 0; width: 340px; height: 185px;
    background: radial-gradient(ellipse at 20% 40%, #f7a21b 0%, #f8c57a 35%, rgba(246,246,246,0) 75%);
  }
  .photo--clinic-tools {
    left: 780px; top: 0; width: 483px; height: 560px;
    background: radial-gradient(ellipse at 60% 55%, #d9d9d9 0%, #e9ece4 40%, rgba(246,246,246,0) 78%);
  }
  .brand-mark {
    position: absolute; left: 400px; top: 60px;
    width: 120px; height: 120px; border-radius: 50%;
    background: var(--leaf-green);
  }
  .brand { position: absolute; left: 466px; top: 48px; }
  .brand__doctor {
    font-family: "Barlow Condensed", sans-serif; font-weight: 500;
    font-size: 22px; color: var(--ink-soft); letter-spacing: 0.5px;
    margin-left: 79px;
  }
  .brand__name {
    font-family: "Barlow Condensed", sans-serif; font-weight: 700;
    font-size: 52px; line-height: 1; color: var(--brand-green);
    letter-spacing: 1px; margin-left: 79px; margin-top: 2px;
  }
  .brand__disciplines {
    font-family: "Barlow Condensed", sans-serif; font-weight: 500;
    font-size: 17px; color: var(--ink-soft); margin-left: 79px; margin-top: 4px;
  }
  .brand__rule {
    margin-left: 79px; margin-top: 6px;
    width: 484px; height: 2px; background: var(--pulse-red);
  }
  .tagline {
    position: absolute; left: 56px; top: 236px;
    font-family: "Montserrat", sans-serif; font-style: italic;
    font-size: 27px; color: var(--tagline-green);
  }
  .services {
    position: absolute; left: 55px; top: 294px;
    display: grid; grid-template-columns: 404px 340px; row-gap: 20px;
    list-style: none;
  }
  .service {
    display: flex; align-items: center; gap: 18px; height: 58px;
    font-family: "Montserrat", sans-serif; font-size: 26px; color: var(--ink);
  }
  .service__icon { width: 58px; height: 58px; flex: none; }
</style>
</head>
<body>
<main class="stage">
  <section class="banner" aria-label="Verdant Care House services banner">
    <div class="photo photo--citrus" role="img" aria-label="Orange slices and glass vitamin ampoules"></div>
    <div class="photo photo--clinic-tools" role="img" aria-label="IV infusion bag, stethoscope, acupuncture needles, mortar with herbs and homoeopathic pills"></div>

    <div class="brand-mark" aria-hidden="true"></div>
    <header class="brand">
      <p class="brand__doctor">Dr. Elena Varghese’s (MBBS, MD)</p>
      <h1 class="brand__name">VERDANT CARE HOUSE</h1>
      <p class="brand__disciplines">Allopathy, Ayurveda, Homeopathy, Acupuncture/Sujok</p>
      <div class="brand__rule"></div>
    </header>

    <p class="tagline">An integrative clinic for health Leaving....Naturally!!</p>

    <ul class="services">
      <li class="service">
        <svg class="service__icon" viewBox="0 0 58 58" aria-hidden="true"><circle cx="29" cy="29" r="29" fill="#8cc63f"/><path d="M29 12 C22 23 18 29 18 35 a11 11 0 0 0 22 0 C40 29 36 23 29 12Z" fill="#fff"/><circle cx="29" cy="36" r="6" fill="#8cc63f"/></svg>
        IV NUTRITION THERAPY
      </li>
      <li class="service">
        <svg class="service__icon" viewBox="0 0 58 58" aria-hidden="true"><circle cx="29" cy="29" r="29" fill="#8cc63f"/><path d="M15 28 h28 a14 12 0 0 1 -28 0Z" fill="#fff"/><path d="M29 26 C27 18 32 13 38 13 C38 20 34 25 29 26Z" fill="#fff"/></svg>
        HOMOEPATHY
      </li>
      <li class="service">
        <svg class="service__icon" viewBox="0 0 58 58" aria-hidden="true"><circle cx="29" cy="29" r="29" fill="#8cc63f"/><path d="M29 12 C22 23 18 29 18 35 a11 11 0 0 0 22 0 C40 29 36 23 29 12Z" fill="#fff"/><circle cx="29" cy="36" r="6" fill="none" stroke="#8cc63f" stroke-width="2.5"/></svg>
        IV VITAMIN C THERAPY
      </li>
      <li class="service">
        <svg class="service__icon" viewBox="0 0 58 58" aria-hidden="true"><circle cx="29" cy="29" r="29" fill="#8cc63f"/><rect x="14" y="33" width="30" height="5" rx="2" fill="#fff"/><path d="M20 32 L38 18" stroke="#fff" stroke-width="3" stroke-linecap="round"/><circle cx="32" cy="28" r="4" fill="#fff"/></svg>
        ACCUPUNCTURE
      </li>
      <li class="service">
        <svg class="service__icon" viewBox="0 0 58 58" aria-hidden="true"><circle cx="29" cy="29" r="29" fill="#8cc63f"/><path d="M29 12 C22 23 18 29 18 35 a11 11 0 0 0 22 0 C40 29 36 23 29 12Z" fill="#fff"/><path d="M24 34 a5 6 0 0 0 5 7" stroke="#8cc63f" stroke-width="2.5" fill="none"/></svg>
        CHELATION THERAPY
      </li>
      <li class="service">
        <svg class="service__icon" viewBox="0 0 58 58" aria-hidden="true"><circle cx="29" cy="29" r="29" fill="#8cc63f"/><circle cx="29" cy="29" r="14" fill="none" stroke="#fff" stroke-width="4"/><circle cx="29" cy="29" r="5" fill="#fff"/></svg>
        AYURVEDA
      </li>
    </ul>
  </section>
</main>
</body>
</html>
```